Sophrologist needs a cool signage at door entrance

I need signage for dr in sophrology based in Belgium (french speaking). The signed should capture the name the "Mireille Vantoorn" - "Naturopathe-Sophrologue-Reiki" and a catchphrase = (Healthy way of life)
« Fais du bien à ton corps, pour que ton âme ait envie d’y rester »
Requirements
Must have
- Hey,
Thats the instagram account for some inspiration www.instagram.com/mireille_serene_wellbeing
Light colors, green, blue
Healthy way of life
Size is 45cm wide on 30 cm high
The signage will be placed in front off woof pannel

```html
<!DOCTYPE html>
<html lang="fr">
<head>
<meta charset="utf-8">
<title>Mireille Vantoorn – Enseigne</title>
<link rel="stylesheet" href="https://fonts.googleapis.com/css2?family=Noto+Serif:ital,wght@0,400;0,700;1,400&family=Sacramento&display=swap">
<style>
  :root {
    --page-bg: #ffffff;
    --sky-white: #ffffff;
    --sky-pale: #bdeeff;
    --sky-light: #5cd3fb;
    --sky-deep: #0aaaf8;
    --edge-violet: #5a55f0;
    --edge-magenta: #ff22e6;
    --name-purple: #7f3c98;
    --ink-dark: #3a4038;
    --frame-gold: #d8b040;
    --frame-red: #c8204a;
    --lotus-pink: #e0407c;
    --lotus-orange: #f28a2a;
    --lotus-red: #d8283a;
    --lotus-purple: #8a3c9c;
  }
  * { margin: 0; padding: 0; box-sizing: border-box; }
  html, body {
    width: 975px;
    height: 1200px;
    overflow: hidden;
    background: var(--page-bg);
  }
  .canvas {
    position: relative;
    width: 975px;
    height: 1200px;
  }
  .sign {
    position: absolute;
    left: 20px;
    top: 288px;
    width: 935px;
    height: 623px;
    overflow: hidden;
    background: radial-gradient(circle at 5% 57%,
      var(--sky-white) 0,
      var(--sky-pale) 120px,
      var(--sky-light) 420px,
      var(--sky-deep) 700px,
      var(--sky-deep) 815px,
      var(--edge-violet) 858px,
      var(--edge-magenta) 915px);
  }
  .sign-frame {
    position: absolute;
    left: 10px;
    top: 10px;
    width: 880px;
    height: 603px;
    border: 1.5px solid;
    border-right: none;
    border-image: linear-gradient(180deg, var(--frame-gold), var(--frame-red)) 1;
    -webkit-mask-image: linear-gradient(90deg, #000 88%, transparent 100%);
    mask-image: linear-gradient(90deg, #000 88%, transparent 100%);
  }
  .sign-name {
    position: absolute;
    left: 106px;
    top: 72px;
    font-family: "Noto Serif", serif;
    font-weight: 700;
    font-size: 90px;
    line-height: 1;
    color: var(--name-purple);
    white-space: nowrap;
    transform: scaleX(0.76);
    transform-origin: left top;
  }
  .sign-profession {
    position: absolute;
    left: 158px;
    top: 214px;
    font-family: "Noto Serif", serif;
    font-style: italic;
    font-weight: 400;
    font-size: 40px;
    line-height: 1;
    color: var(--ink-dark);
    white-space: nowrap;
    transform: scaleX(0.8);
    transform-origin: left top;
  }
  .sign-motto {
    position: absolute;
    left: 100px;
    top: 372px;
    width: 440px;
    font-family: "Sacramento", cursive;
    font-size: 38px;
    line-height: 36px;
    color: var(--ink-dark);
    text-align: center;
    white-space: nowrap;
  }
  .sign-lotus {
    position: absolute;
    left: 545px;
    top: 305px;
    width: 320px;
    height: 220px;
    border-radius: 50% 50% 45% 45%;
    background:
      radial-gradient(ellipse at 60% 50%, var(--lotus-red) 0, var(--lotus-orange) 22%, var(--lotus-pink) 42%, var(--lotus-purple) 62%, rgba(138, 60, 156, 0) 75%);
  }
</style>
</head>
<body>
  <main class="canvas">
    <section class="sign">
      <div class="sign-frame"></div>
      <h1 class="sign-name">Mireille Vantoorn</h1>
      <p class="sign-profession">Naturopathe-Sophrologue-Reiki</p>
      <p class="sign-motto">Fais du bien à ton corps,<br>pour que ton âme ait envie d’y rester</p>
      <div class="sign-lotus" role="img" aria-label="Emblème : fleur de lotus rose et orange posée sur une courbe violette"></div>
    </section>
  </main>
</body>
</html>
```